New Web Design Project

Details for my new Web Design Project will be added soon.
Updates
This is my website that need to be work into it www.marlowesquest.com
I am really frustrated with your company, we really need a refund of $556.00 as soon as possible, Do not feel safe to work with.

```html
<!DOCTYPE html>
<html lang="en">
<head>
<meta charset="utf-8">
<title>Marlowe's Quest</title>
<link href="https://fonts.googleapis.com/css2?family=Oswald:wght@400;500&family=Arimo:wght@400;700&family=Tinos:ital,wght@0,400;0,700;1,400;1,700&display=swap" rel="stylesheet">
<style>
:root{
  --pink:#ee3f8a;
  --pink-soft:#f06aa6;
  --ink:#1b1b1b;
  --grey:#777;
  --line:#e3e3e3;
  --panel:#f3f3f3;
  --nav:#1e1e1e;
}
*{box-sizing:border-box;margin:0;padding:0}
html,body{width:814px;height:1200px;overflow:hidden;background:#fff}
body{position:relative;font-family:Arimo,Arial,sans-serif;color:var(--ink);font-size:8px}
.abs{position:absolute}
a{color:inherit;text-decoration:none}
.topbar{left:0;top:0;width:814px;height:27px;background:#fafafa;border-top:2px solid var(--pink);font-family:Oswald,sans-serif;font-size:7px;letter-spacing:.2px}
.topbar span{position:absolute;top:8px}
.pinktxt{color:var(--pink)}
.sq{display:inline-block;width:11px;height:11px;border-radius:2px;vertical-align:middle;margin-left:2px}
.brand{left:44px;top:47px;display:flex;align-items:center;gap:8px}
.brand .mark{width:34px;height:34px;background:var(--pink);border-radius:50%}
.brand .name{font-family:Arimo,sans-serif;font-weight:700;font-size:17px;line-height:17px;color:var(--pink);text-transform:uppercase}
.account{left:457px;top:27px;width:345px;height:72px;background:#efefef;font-family:Oswald,sans-serif;font-size:7px}
.account span{position:absolute}
.field{position:absolute;height:12px;background:#fff;border:1px solid #999;font-family:Arimo,sans-serif;font-size:6px;color:#777;padding:2px 4px}
.btn{display:inline-block;background:var(--pink);color:#fff;font-family:Arimo,sans-serif;font-weight:700;text-transform:uppercase;text-align:center}
.nav{left:0;top:107px;width:814px;height:26px;background:linear-gradient(#3a3a3a,#111);font-family:Oswald,sans-serif;font-size:9.5px;color:#fff;text-transform:uppercase}
.nav span{position:absolute;top:0;height:26px;line-height:26px;text-align:center}
.nav .on{background:var(--pink)}
.card-box{border:1px solid var(--line);border-bottom:2px solid var(--pink);background:#fff}
.photo{border-radius:2px}
.welcome h1{font-family:Arimo,sans-serif;font-weight:400;font-size:25px;letter-spacing:2px}
.serif{font-family:Tinos,serif}
.pod-head{background:linear-gradient(#fafafa,#e8e8e8);text-align:center;font-family:Tinos,serif;font-size:10.5px;height:26px;line-height:26px;text-transform:uppercase}
.cat{color:#aaa;font-size:8px;text-transform:uppercase}
.pname{font-size:8.5px;border-bottom:1px solid var(--ink);padding-bottom:1px;display:inline-block}
.stars{color:var(--pink);font-size:8px;letter-spacing:1px}
.stars small{color:var(--ink);font-size:6.5px;letter-spacing:0}
.tabs{font-family:Oswald,sans-serif;font-size:9.5px;text-transform:uppercase}
.product{width:178px;height:242px}
.product .photo{position:absolute;left:47px;top:6px;width:84px;height:132px}
.product .cat{position:absolute;left:11px;top:148px}
.product .pname{position:absolute;left:11px;top:161px}
.product .price{position:absolute;left:11px;top:180px;font-size:8px}
.product .stars{position:absolute;left:11px;top:193px}
.product .btn{position:absolute;top:213px;width:76px;height:17px;line-height:17px;font-size:8px}
.product .stock{position:absolute;left:11px;top:217px;color:var(--pink-soft);font-size:8px}
.acc{width:120px;height:150px}
.acc .photo{position:absolute;left:14px;top:0;width:64px;height:58px}
.acc .pname{position:absolute;left:0;top:72px;font-size:9px}
.acc .sub{position:absolute;left:0;top:92px;color:#666;font-size:8px}
.acc .price{position:absolute;left:0;top:104px;font-size:8px}
.acc .btn{position:absolute;left:0;top:122px;width:76px;height:17px;line-height:17px;font-size:8px}
.arrow{width:14px;height:28px;background:var(--pink)}
.info{height:126px;border:1px solid var(--line);background:#fff}
.info .head{height:25px;background:linear-gradient(#fafafa,#ececec);font-family:Tinos,serif;font-size:10.5px;line-height:25px;padding-left:11px;text-transform:uppercase;position:relative}
.info .head i{position:absolute;right:10px;top:7px;width:11px;height:11px;border-radius:50%;background:#ccc}
.more{color:var(--pink);font-size:7.5px;font-weight:700;text-transform:uppercase}
.follow{left:27px;top:1132px;width:760px;height:27px;background:#f1f1f1}
.footer{left:0;top:1172px;width:814px;font-size:7px}
</style>
</head>
<body>

<header>
  <div class="abs topbar">
    <span style="left:37px">CHOOSE &nbsp;Currency &nbsp;<i class="sq" style="background:#b7c4dd;width:9px;height:7px"></i> USD$ ▾</span>
    <span style="left:148px">Language: English ▾</span>
    <span class="pinktxt" style="left:518px">FREE USA SHIPPING! &nbsp;| &nbsp;35% SHIPPING COUPON CODE</span>
    <span style="left:688px">SHARE <i class="sq" style="background:#3b5998"></i><i class="sq" style="background:#55acee"></i><i class="sq" style="background:var(--pink)"></i> ▾</span>
  </div>

  <div class="abs brand"><span class="mark"></span><span class="name">Marlowe's<br>Quest</span></div>

  <div class="abs account">
    <span style="left:14px;top:15px">Customer Care ▸ &nbsp;| &nbsp; My Wish List &nbsp;| &nbsp; Track Order ▾ &nbsp;| &nbsp; Request a Catalogue &nbsp;| &nbsp;<b class="pinktxt">▪</b> Live Chat ▾</span>
    <span style="left:14px;top:33px">Join &nbsp; | &nbsp; Sign In</span>
    <span class="pinktxt" style="left:273px;top:39px">View Bag/ Checkout</span>
    <div class="field" style="left:11px;top:52px;width:104px">Search entire store here...</div>
    <div class="field" style="left:122px;top:52px;width:84px">All Categories</div>
    <span class="btn" style="left:213px;top:52px;width:35px;height:12px;line-height:12px;font-size:6px;font-weight:400;text-transform:none">Search</span>
    <span style="left:260px;top:53px;font-family:Arimo,sans-serif;font-size:7px"><b class="pinktxt">■</b> &nbsp;Item: 0 &nbsp;Total: $0.00</span>
  </div>

  <nav class="abs nav">
    <span class="on" style="left:38px;width:75px">Home</span>
    <span style="left:120px;width:70px">Dresses <b class="pinktxt">▾</b></span>
    <span style="left:198px;width:70px">Pants <b class="pinktxt">▾</b></span>
    <span style="left:280px;width:80px">Shorts &amp; Skirts</span>
    <span style="left:372px;width:78px">Gymnastic</span>
    <span style="left:455px;width:60px">Jackets</span>
    <span style="left:525px;width:75px">Accessories</span>
    <span class="on" style="left:609px;width:75px">Coupons</span>
  </nav>
</header>

<main>
  <section class="abs card-box welcome" style="left:19px;top:156px;width:525px;height:236px">
    <div class="abs photo" role="img" aria-label="Figure skater in a blue competition dress" style="left:50px;top:4px;width:110px;height:228px;background:linear-gradient(#eaf2f8,#bcd6e6)"></div>
    <h1 class="abs" style="left:219px;top:12px">WELCOME TO</h1>
    <div class="abs" style="left:221px;top:48px;display:flex;align-items:center;gap:8px">
      <span style="width:28px;height:28px;background:var(--pink);border-radius:50%"></span>
      <span style="font-weight:700;font-size:15px;line-height:15px;color:var(--pink);text-transform:uppercase">Marlowe's<br>Quest</span>
    </div>
    <div class="abs serif" style="left:434px;top:27px;width:53px;height:53px;border-radius:50%;background:var(--pink);color:#fff;text-align:center;line-height:14px;padding-top:10px"><b style="font-size:17px">#1</b><br><span style="font-size:11px">SITE</span></div>
    <div class="abs" style="left:219px;top:102px;width:193px;height:2px;background:var(--pink)"></div>
    <p class="abs serif" style="left:219px;top:114px;width:287px;font-size:10px;line-height:14.5px;font-style:italic;text-align:justify"><b>Marlowe's Quest</b> specializes in designing and creating high-end designed competition figure skating dresses and costumes for figure skaters including baton twirling, majorettes, drill team uniforms, or dancer costumes in United States.</p>
    <p class="abs serif" style="left:219px;top:180px;font-size:10px">Need a Customized Look? Contact us!</p>
    <span class="abs more" style="left:219px;top:202px;font-weight:400;font-size:7.5px">Read More ▸</span>
  </section>

  <aside class="abs card-box" style="left:558px;top:155px;width:245px;height:236px">
    <div class="pod-head">Product of the Day</div>
    <div class="abs photo" role="img" aria-label="Flame print yoga capri pants" style="left:16px;top:52px;width:52px;height:110px;background:linear-gradient(#e85a1a,#1b1b1b)"></div>
    <span class="abs cat" style="left:102px;top:54px">Yoga Pant</span>
    <span class="abs pname" style="left:102px;top:70px;width:135px;font-size:9px;line-height:16px;border:none;text-decoration:underline">Skirtpants Yoga Capri All Black MQ</span>
    <span class="abs" style="left:102px;top:103px;font-size:8px">Our Price: $49.99</span>
    <span class="abs stars" style="left:102px;top:119px">★★★★★ <small>(10 reviews)</small></span>
    <span class="abs" style="left:102px;top:141px;color:var(--pink-soft);font-size:8px">In of Stock!</span>
    <span class="abs btn" style="left:102px;top:158px;width:76px;height:17px;line-height:17px;font-size:8px">Shop Now</span>
    <span class="abs" style="left:108px;top:211px;display:flex;gap:5px"><i style="width:7px;height:7px;border-radius:50%;background:#999"></i><i style="width:7px;height:7px;border-radius:50%;background:var(--pink)"></i><i style="width:7px;height:7px;border-radius:50%;background:#999"></i></span>
  </aside>

  <div class="abs tabs" style="left:32px;top:426px;width:755px;height:20px;border-bottom:1px solid var(--line)">
    <span class="abs" style="left:0;top:1px;font-size:10px">☰</span>
    <span class="abs" style="left:18px;top:0;border-bottom:2px solid var(--pink);padding-bottom:3px">Featured Products</span>
    <span class="abs" style="left:126px;top:0">New Arrivals</span>
    <span class="abs" style="left:211px;top:0">Deals of the Week</span>
  </div>

  <section>
    <article class="abs card-box product" style="left:30px;top:466px">
      <div class="photo" role="img" aria-label="Black skirted yoga capri" style="background:linear-gradient(#555,#111)"></div>
      <span class="abs btn" style="left:42px;top:62px;width:90px;height:21px;line-height:21px;font-size:8px;background:var(--pink-soft)">Quick View</span>
      <span class="cat">Yoga Pant</span><span class="pname">Skirtpants Yoga Capri All Black MQ</span>
      <span class="price">Our Price: $49.99</span><span class="stars">★★★★★ <small>(10 reviews)</small></span>
      <span class="btn" style="left:11px">Shop Now</span>
    </article>
    <article class="abs card-box product" style="left:220px;top:466px">
      <div class="photo" role="img" aria-label="Flame print yoga capri" style="background:linear-gradient(#e85a1a,#1b1b1b)"></div>
      <span class="cat">Yoga Pant</span><span class="pname">Skirtpants Yoga Capri All Black MQ</span>
      <span class="price">Our Price: $49.99</span><span class="stars">★★★★★ <small>(10 reviews)</small></span>
      <span class="stock">6 left!</span><span class="btn" style="left:81px">Shop Now</span>
    </article>
    <article class="abs card-box product" style="left:409px;top:466px">
      <div class="photo" role="img" aria-label="Black skirted yoga capri" style="background:linear-gradient(#555,#111)"></div>
      <span class="cat">Yoga Pant</span><span class="pname">Skirtpants Yoga Capri All Black MQ</span>
      <span class="price">Our Price: $49.99</span><span class="stars">★★★★★ <small>(10 reviews)</small></span>
      <span class="stock">Out of Stock!</span><span class="btn" style="left:81px">Shop Now</span>
    </article>
    <article class="abs card-box product" style="left:598px;top:466px">
      <div class="photo" role="img" aria-label="Flame print yoga capri" style="background:linear-gradient(#e85a1a,#1b1b1b)"></div>
      <span class="cat">Yoga Pant</span><span class="pname">Skirtpants Yoga Capri All Black MQ</span>
      <span class="price">Our Price: $49.99</span><span class="stars">★★★★★ <small>(10 reviews)</small></span>
      <span class="stock">Out of Stock!</span><span class="btn" style="left:81px">Shop Now</span>
    </article>
    <span class="abs" style="left:694px;top:722px;font-style:italic;text-decoration:underline;font-size:8px;color:#444">View More Products</span><span class="abs" style="left:770px;top:722px;font-size:7px">▸</span>
  </section>

  <section>
    <div class="abs" style="left:16px;top:762px;width:322px;border-top:3px double #ccc"></div>
    <h2 class="abs serif" style="left:353px;top:754px;font-size:12px;font-weight:400;letter-spacing:1px">ACCESSORIES</h2>
    <div class="abs" style="left:472px;top:762px;width:322px;border-top:3px double #ccc"></div>

    <span class="abs arrow" style="left:15px;top:845px;border-radius:14px 0 0 14px"></span>
    <span class="abs arrow" style="left:781px;top:845px;border-radius:0 14px 14px 0"></span>

    <div class="abs acc" style="left:59px;top:788px"><div class="photo" role="img" aria-label="Purple skate boot cover" style="background:linear-gradient(#6a4fd0,#2d1f7a)"></div><span class="pname">MQ BOOT COVER MQ</span><span class="sub">In Boot Covers</span><span class="price">Our Price: $15.99</span><span class="btn">Shop Now</span></div>
    <div class="abs acc" style="left:206px;top:790px"><div class="photo" role="img" aria-label="Zebra print skate boot cover" style="background:linear-gradient(#d8d8d8,#333)"></div><span class="pname">MQ BOOT COVER MQ</span><span class="sub">In Boot Covers</span><span class="price">Our Price: $15.99</span><span class="btn">Shop Now</span></div>
    <div class="abs acc" style="left:355px;top:790px"><div class="photo" role="img" aria-label="Purple skate boot cover" style="background:linear-gradient(#6a4fd0,#2d1f7a)"></div><span class="pname">MQ BOOT COVER MQ</span><span class="sub">In Boot Covers</span><span class="price">Our Price: $15.99</span><span class="btn">Shop Now</span></div>
    <div class="abs acc" style="left:510px;top:790px"><div class="photo" role="img" aria-label="Zebra print skate boot cover" style="background:linear-gradient(#d8d8d8,#333)"></div><span class="pname">MQ BOOT COVER MQ</span><span class="sub">In Boot Covers</span><span class="price">Our Price: $15.99</span><span class="btn">Shop Now</span></div>
    <div class="abs acc" style="left:657px;top:790px"><div class="photo" role="img" aria-label="Purple skate boot cover" style="background:linear-gradient(#6a4fd0,#2d1f7a)"></div><span class="pname">MQ BOOT COVER MQ</span><span class="sub">In Boot Covers</span><span class="price">Our Price: $15.99</span><span class="btn">Shop Now</span></div>

    <span class="abs" style="left:729px;top:942px;font-style:italic;text-decoration:underline;font-size:8px;color:#444">Shop More</span><span class="abs" style="left:772px;top:942px;font-size:7px">▸</span>
  </section>

  <section>
    <div class="abs info" style="left:27px;top:980px;width:246px">
      <div class="head">How to Take Measures<i></i></div>
      <div class="abs photo" role="img" aria-label="Blue measuring tape" style="left:8px;top:38px;width:118px;height:70px;background:linear-gradient(#d7e8f6,#3f8fd2)"></div>
      <p class="abs" style="left:138px;top:34px;font-size:17px;line-height:19px;text-align:center;width:100px;white-space:nowrap">DOING IT<br>RIGHT</p>
      <div class="abs" style="left:137px;top:78px;width:99px;height:1px;background:#ccc"></div>
      <p class="abs" style="left:137px;top:84px;color:#888;font-size:7.5px;line-height:9px">TAKE YOUR MEASURES<br>CORRECTLY</p>
      <span class="abs more" style="left:174px;top:110px">Learn More ▸</span>
    </div>
    <div class="abs info" style="left:284px;top:980px;width:246px">
      <div class="head">About Us<i></i></div>
      <div class="abs photo" role="img" aria-label="Girl holding figure skates" style="left:14px;top:34px;width:104px;height:82px;background:linear-gradient(#f4e6ec,#c9a9b7)"></div>
      <p class="abs" style="left:140px;top:42px;font-family:Oswald,sans-serif;font-size:14px;width:90px;text-align:center">WHO WE ARE</p>
      <div class="abs" style="left:129px;top:64px;width:106px;height:1px;background:#ccc"></div>
      <p class="abs" style="left:129px;top:70px;color:#888;font-size:7.5px;line-height:9px">WE ARE APPASSIONATED<br>ABOUT FIGURE SKATING</p>
      <span class="abs more" style="left:172px;top:110px">Learn More ▸</span>
    </div>
    <div class="abs info" style="left:542px;top:980px;width:246px">
      <div class="head">Contact Us<i></i></div>
      <p class="abs serif" style="left:11px;top:36px;color:var(--pink);font-style:italic;font-weight:700;font-size:12.5px">CUSTOMER SERVICE</p>
      <p class="abs" style="left:12px;top:61px;font-size:8px"><b class="pinktxt">✆</b> &nbsp;0800 555 0147</p>
      <p class="abs" style="left:12px;top:76px;font-size:8px"><b class="pinktxt">✉</b> &nbsp;info@marlowesquest.com</p>
      <span class="abs" style="left:12px;top:98px"><i class="sq" style="background:#3b5998;margin:0"></i><i class="sq" style="background:#55acee"></i></span>
      <div class="abs photo" role="img" aria-label="Customer service agent with headset" style="left:150px;top:28px;width:62px;height:97px;background:linear-gradient(#efe6dc,#ffffff)"></div>
    </div>
  </section>
</main>

<footer>
  <div class="abs follow">
    <span class="abs" style="left:32px;top:8px"><i class="sq" style="background:#3b5998;margin:0"></i><i class="sq" style="background:#55acee"></i><i class="sq" style="background:var(--pink)"></i></span>
    <span class="abs serif" style="left:87px;top:8px;font-size:10px">FOLLOW US FOR SPECIAL OFFERS!</span>
    <span class="abs" style="left:425px;top:9px;font-size:7.5px"><b class="serif" style="font-size:9.5px">ALERT</b> Get Weekly Updates and Promotions!</span>
    <div class="abs" style="left:590px;top:7px;width:94px;height:13px;background:#fff;border:1px solid #ddd"></div>
    <span class="abs btn" style="left:688px;top:7px;width:61px;height:13px;line-height:13px;font-size:7.5px;font-weight:400;text-transform:none">Subscribe</span>
  </div>
  <div class="abs footer">
    <span class="abs" style="left:56px;top:0">Copyright 2014 Marlowe's Quest . <span style="color:#555">All rights reserved</span></span>
    <span class="abs" style="left:287px;top:0">Customer Care: Free Phone 0800 555 0147 &nbsp;| &nbsp;Contact Us &nbsp;| &nbsp;Track My Order &nbsp;| &nbsp;Feedback &nbsp;| &nbsp;Sitemap</span>
  </div>
</footer>

</body>
</html>
```